Tampa, Florida based Real Estate company Business Cards

Need ideas for real estate business cards
Updates

Need extra days to review

Industry/Entity Type

Real Estate

Contact Information for Business Card

Space for image, space for logo, contact information space

Font styles to use
Sans Serif

Colors

Designer to choose colors to be used in the design.

Requirements
Must have
• Options to have duplicate content on the back of card for a team of agents.

```html
<!DOCTYPE html>
<html lang="en">
<head>
<meta charset="utf-8">
<title>Harbor Crest Realty – Business Cards</title>
<link rel="stylesheet" href="https://fonts.googleapis.com/css2?family=Raleway:wght@400;500;800&display=swap">
<style>
  :root {
    --navy: #000059;
    --steel: #a2b2b1;
    --steel-soft: #5f6f86;
    --paper: #ffffff;
    --backdrop: #c9c9c9;
    --edge: #1a1a1a;
  }
  * { margin: 0; padding: 0; box-sizing: border-box; }
  html, body {
    width: 1200px; height: 846px; overflow: hidden;
    background: var(--backdrop);
    font-family: "Raleway", sans-serif;
  }
  .card {
    position: absolute;
    left: 346px;
    width: 508px;
    height: 290px;
    overflow: hidden;
  }
  .card-front {
    top: 113px;
    background: var(--paper);
    border: 1px solid var(--edge);
  }
  .card-back {
    top: 443px;
    background: var(--navy);
  }
  .brand-front {
    position: absolute;
    left: 40px; top: 128px;
    width: 170px;
    text-align: center;
    color: var(--navy);
    font-weight: 500;
    line-height: 1.15;
    white-space: nowrap;
  }
  .brand-front .brand-name { display: block; font-size: 17px; letter-spacing: 0.5px; }
  .brand-front .brand-tag { display: block; font-size: 10px; letter-spacing: 6px; padding-left: 6px; margin-top: 4px; }
  .divider {
    position: absolute;
    left: 229px; top: 101px;
    width: 1px; height: 90px;
    background: var(--steel);
  }
  .contact {
    position: absolute;
    left: 252px; top: 97px;
    color: var(--navy);
    white-space: nowrap;
  }
  .agent-name {
    font-size: 16.5px;
    font-weight: 800;
    margin-bottom: 5px;
  }
  .contact-list { list-style: none; }
  .contact-list li {
    position: relative;
    padding-left: 18px;
    font-size: 14px;
    line-height: 18.3px;
    font-weight: 400;
  }
  .contact-list svg {
    position: absolute;
    left: 0; top: 4px;
    width: 11px; height: 11px;
  }
  .brand-back {
    position: absolute;
    left: 0; right: 0; top: 44px;
    text-align: center;
    color: var(--steel);
    font-weight: 500;
    line-height: 1.1;
  }
  .brand-back .brand-name { display: block; font-size: 36px; letter-spacing: 3px; }
  .brand-back .brand-tag { display: block; font-size: 17px; letter-spacing: 14px; margin-top: 4px; padding-left: 14px; }
  .bridge-art {
    position: absolute;
    left: 0; right: 0; bottom: 0;
    height: 148px;
    background: linear-gradient(to bottom, var(--navy) 0%, var(--steel-soft) 70%, var(--steel) 100%);
  }
</style>
</head>
<body>
  <section class="card card-front">
    <div class="brand-front">
      <span class="brand-name">HARBOR CREST</span>
      <span class="brand-tag">REALTY</span>
    </div>
    <div class="divider"></div>
    <div class="contact">
      <p class="agent-name">Name Lastname</p>
      <ul class="contact-list">
        <li>
          <svg viewBox="0 0 12 12" aria-hidden="true"><path d="M4 1 L6 1 L6.5 3.5 L5 4.5 Q5.5 7 7.5 8 L8.5 6.8 L11 7.5 L11 9.5 Q10 11 8 10.8 Q2 9 1.2 3 Q1.5 1.2 4 1 Z" fill="var(--navy)"/></svg>
          Office number: 813-555-0142
        </li>
        <li>
          <svg viewBox="0 0 12 12" aria-hidden="true" fill="none" stroke="var(--navy)" stroke-width="1"><circle cx="6" cy="6" r="5"/><ellipse cx="6" cy="6" rx="2.2" ry="5"/><path d="M1 6 H11 M1.8 3.5 H10.2 M1.8 8.5 H10.2"/></svg>
          www.harborcrestrealty.com
        </li>
        <li>
          <svg viewBox="0 0 12 12" aria-hidden="true"><path d="M6 0.5 A4 4 0 0 1 10 4.5 C10 7.5 6 11.5 6 11.5 C6 11.5 2 7.5 2 4.5 A4 4 0 0 1 6 0.5 Z M6 3 A1.5 1.5 0 1 0 6 6 A1.5 1.5 0 1 0 6 3 Z" fill="var(--navy)" fill-rule="evenodd"/></svg>
          1450 Palmetto Shore Ave<br>Tampa, FL 33611
        </li>
      </ul>
    </div>
  </section>

  <section class="card card-back">
    <div class="brand-back">
      <span class="brand-name">HARBOR CREST</span>
      <span class="brand-tag">REALTY</span>
    </div>
    <div class="bridge-art" role="img" aria-label="Illustration of a cable-stayed bay bridge with two towers spanning the card"></div>
  </section>
</body>
</html>
```